ONE PAGE WEB DESIGN NEEDED for Finance Company

We need a web design (ONE PAGE DESIGN ONLY) for a new finance website called Corvella Lending. Corvella Lending helps customers get the right loan, whether its a home loan, investment loan, business loan etc.

You are required to come up with just the homepage design. Professionalism and quality is the key factors in the successful design.

Here are a few design questions to help you out:

-
What information should be used on the page?
Ive provided a document which outlines all the information needed to put on homepage (attached to the brief - called corvella_page_info). Also see the Must Have section below on this brief.

-
What links should appear in the navigation/footer?:
The navigation should provide links to the following pages (NOTE: services link has subcategories):
1 Homepage
2 Services
- Home loans
- Investment loans
- Refinancing loans
- Business loans
3 About Us
4 FAQ
5 Contact Us

-
What colors should be used in the design?
Our company colors - Cyan: #2EADE3, Blue: #004B70, White. Feel free to submit designs with slight variations if you feel it improves the design.

-
What should the layout of the page be?
This is up to you to come up with - we are open to different layouts for the page design (as long as they capture the information effectively and making it easy to understand).

Target Market(s)

Potential Home owners, Families and Business Owners

Industry/Entity Type

Business

Requirements
Must have
• - Must contain our logo (attached as PNG and Illustrator file)
- Winning designer must supply a Photoshop file (PSD) that will allow us.
Nice to have
• - Should include photos/images of families, professional groups, tradespeople etc (you can use stock photos from PixelVaultImages and I will purchase them once you are selected as the winning design)
- Link to a loan calculator somewhere on front page with a button 'Find out how much you could borrow' (or maybe even try adding a loan calculator to the homepage if you think this would look good)
- Page should have a main headline "Finding the right loan for you" or "Corvella Lending finds the right loan for our customers."
- Must include Accreditation logos somewhere on the homepage (will try and supply these soon)
Should not have
• - Poor quality designs will not be considered
- Do not use clipart

```html
<!DOCTYPE html>
<html lang="en">
<head>
<meta charset="utf-8">
<title>Corvella Lending — Finding the right loan for you</title>
<link rel="stylesheet" href="https://fonts.googleapis.com/css2?family=Arimo:wght@400;700&family=Ubuntu:wght@400;500;700&display=swap">
<style>
:root{
  --cyan:#2eade3;
  --cyan-light:#5fc3ee;
  --blue:#004b70;
  --blue-mid:#0f6d9c;
  --nav-top:#2a8fc4;
  --nav-bottom:#0c5f8c;
  --text:#2b2b2b;
  --muted:#6a6a6a;
  --line:#dfe5ea;
  --page:#f4f6f8;
  --white:#ffffff;
}
*{box-sizing:border-box;margin:0;padding:0}
html,body{width:1200px;height:2368px;overflow:hidden}
body{position:relative;background:linear-gradient(#fbfcfd,var(--page) 400px,var(--page));font-family:"Arimo",Arial,sans-serif;color:var(--text)}
.abs{position:absolute}

/* header */
.brand{left:50px;top:40px;width:300px}
.brand-mark{width:62px;height:62px;border-radius:50%;border:6px solid var(--cyan);margin-left:86px}
.brand-name{font-family:"Ubuntu",sans-serif;font-weight:500;font-size:38px;color:var(--cyan);letter-spacing:-1px;margin-top:30px;line-height:1}
.brand-tag{font-family:"Ubuntu",sans-serif;font-size:15px;color:var(--blue);margin-top:10px;letter-spacing:.3px}
.call{right:50px;top:92px;font-family:"Arimo",sans-serif;font-weight:700;font-style:italic;font-size:18px;color:var(--cyan)}
.call b{color:var(--blue)}
.search{left:823px;top:162px;width:327px;height:40px;border-radius:6px;background:var(--white);border:2px solid #d6dde3;box-shadow:inset 0 2px 3px rgba(0,0,0,.08)}
.search span{position:absolute;left:16px;top:10px;font-size:14px;font-style:italic;color:#9aa3aa}
.search-btn{position:absolute;right:-2px;top:-2px;width:42px;height:40px;border-radius:6px;background:linear-gradient(var(--cyan-light),var(--blue-mid))}

/* navigation */
.nav{left:0;top:237px;width:1200px;height:71px;background:linear-gradient(var(--nav-top),var(--nav-bottom));box-shadow:0 3px 6px rgba(0,0,0,.2)}
.nav ul{list-style:none;display:flex;position:absolute;left:50px;top:0}
.nav li{width:220px;height:71px;line-height:71px;text-align:center;color:var(--white);font-family:"Ubuntu",sans-serif;font-size:17px;text-transform:uppercase;border-right:1px solid rgba(255,255,255,.12)}
.nav li.active{background:linear-gradient(#4cc0ee,#1a8bc4)}
.dropdown{left:270px;top:308px;width:220px;background:var(--white);box-shadow:0 4px 10px rgba(0,0,0,.18);z-index:5;padding:6px 0}
.dropdown a{display:block;padding:0 22px;height:40px;line-height:40px;color:var(--blue);font-size:16px;text-decoration:none;border-bottom:1px solid var(--line)}
.dropdown a:last-child{border-bottom:0}

/* hero */
.hero{left:50px;top:322px;width:1100px;height:452px;background:linear-gradient(90deg,#ffffff 0%,#c7d5dc 12%,#6b8592 35%,#8ea86a 70%,#7fa0b8 100%);overflow:hidden}
.hero-sky{position:absolute;left:0;top:0;width:1100px;height:452px;background:linear-gradient(#9dc4e6 0%,#6a7e86 38%,#5b7a42 78%,#3f6a2a 100%);opacity:.65}
.hero-fade{position:absolute;left:0;top:0;width:140px;height:452px;background:linear-gradient(90deg,#fff,rgba(255,255,255,0))}
.hero-panel{left:89px;top:359px;width:320px;height:328px;background:rgba(70,90,102,.82);border-radius:4px;box-shadow:0 2px 8px rgba(0,0,0,.3);padding:24px 34px}
.hero-panel h2{font-family:"Arimo",sans-serif;font-weight:700;font-size:38px;color:var(--cyan);border-bottom:3px solid var(--cyan);padding-bottom:2px;width:250px}
.hero-panel ul{list-style:none;margin-top:14px}
.hero-panel li{color:var(--white);font-size:25px;height:57px;display:flex;align-items:center;gap:18px}
.hero-panel li svg{flex:none}
.btn-small{display:inline-block;background:linear-gradient(var(--cyan-light),var(--cyan));color:var(--white);font-size:13px;font-weight:700;padding:10px 22px;border-radius:3px;margin-top:20px}
.dots{right:62px;top:732px;display:flex;gap:8px}
.dots i{width:18px;height:18px;border-radius:50%;background:var(--blue-mid);border:2px solid #9fd8f2}
.dots i.on{background:var(--cyan)}

/* welcome */
.welcome{left:50px;top:810px;width:1100px}
.welcome h1{font-family:"Ubuntu",sans-serif;font-weight:500;font-size:24px;color:var(--blue);letter-spacing:.5px}
.welcome p{font-size:16.5px;line-height:26px;margin-top:28px;color:var(--text)}
.welcome p:first-of-type{margin-top:24px}
.welcome strong{color:var(--blue)}
.welcome em{color:var(--blue);font-weight:700;text-decoration:underline}
.divider{left:50px;top:1224px;width:1100px;height:1px;background:#d5dbe0}

/* offers panel */
.offers{left:50px;top:1259px;width:1098px;height:660px;background:var(--white);border:1px solid #dde3e8;box-shadow:0 2px 4px rgba(0,0,0,.06)}
.offers-head{height:59px;background:linear-gradient(#4fbfec,var(--cyan));text-align:center;line-height:59px;color:var(--white);font-family:"Ubuntu",sans-serif;font-weight:500;font-size:27px;font-variant:small-caps;letter-spacing:.5px}
.offers-glow{left:50px;top:1560px;width:1098px;height:110px;background:radial-gradient(ellipse at center,rgba(46,173,227,.22),rgba(46,173,227,0) 70%)}
.card{top:1354px;width:219px;height:371px;border-radius:10px;background:linear-gradient(#ffffff,#f4f6f7 55%,#dcdfe1);border:1px solid #e4e8eb;box-shadow:0 6px 8px rgba(0,0,0,.18);padding:20px 26px}
.card h3{font-family:"Arimo",sans-serif;font-weight:700;font-size:29px;line-height:36px;color:var(--blue-mid)}
.card ul{list-style:none;margin-top:22px}
.card li{font-size:15.5px;line-height:30px;color:#444;padding-left:18px;position:relative}
.card li::before{content:"";position:absolute;left:0;top:10px;border-left:7px solid var(--cyan);border-top:5px solid transparent;border-bottom:5px solid transparent}
.card .more{position:absolute;left:26px;bottom:22px;font-size:14px;font-weight:700;color:var(--blue)}
.card .more::after{content:" ▸";font-size:11px}
.borrow{left:389px;top:1767px;width:418px;height:116px;border-radius:8px;background:linear-gradient(#2a87b7,var(--blue));border:3px solid #5fc3ee;display:flex;align-items:center;gap:22px;padding-left:22px}
.borrow span{font-family:"Ubuntu",sans-serif;font-weight:700;font-size:27px;line-height:33px;color:var(--white)}

/* bottom boxes */
.box{top:1964px;height:286px;background:var(--white);border:1px solid #dde3e8;border-radius:6px;box-shadow:0 2px 4px rgba(0,0,0,.06);overflow:hidden}
.box-head{height:55px;line-height:55px;padding-left:36px;background:linear-gradient(#2a8fc4,var(--blue));color:var(--white);font-family:"Ubuntu",sans-serif;font-weight:500;font-size:17px}
.box-body{padding:16px 24px;font-size:13.5px;line-height:19px;color:#333}
.box .btn-small{position:absolute;right:30px;bottom:14px;padding:6px 18px;font-size:12px;margin:0;border-radius:4px}
.sign{text-align:right;margin-top:40px;font-weight:700;color:var(--blue)}
.sign small{display:block;font-weight:400;color:var(--muted);font-size:13px}
.news-item{padding:6px 0 16px;border-bottom:1px solid var(--line)}
.news-item + .news-item{border:0;padding-top:14px}
.news-date{color:var(--cyan)}
.contact-body{padding:16px 30px}
.contact-body p{margin-bottom:22px}
.contact-body a,.contact-body .hl{color:var(--blue-mid)}

/* footer */
.footer{left:0;top:2296px;width:1200px;height:72px;background:var(--blue);color:var(--white);font-size:12.5px}
.footer .copy{position:absolute;left:50px;top:28px;color:var(--cyan)}
.footer nav{position:absolute;left:230px;top:28px;display:flex}
.footer nav span{padding:0 22px;border-left:1px solid rgba(255,255,255,.35)}
.footer nav span:first-child{border-left:0}
.footer .follow{position:absolute;right:30px;top:22px;display:flex;align-items:center;gap:10px}
.footer .follow i{width:20px;height:20px;border-radius:3px;background:var(--cyan)}
</style>
</head>
<body>

<header>
  <div class="brand abs">
    <div class="brand-mark" aria-hidden="true"></div>
    <div class="brand-name">Corvella Lending</div>
    <div class="brand-tag">FINDING THE RIGHT LOAN FOR YOU</div>
  </div>
  <div class="call abs">Call Us: <b>1800 555 210</b></div>
  <div class="search abs">
    <span>search</span>
    <div class="search-btn">
      <svg width="42" height="40" viewBox="0 0 42 40"><circle cx="19" cy="18" r="7" fill="none" stroke="#fff" stroke-width="3"/><line x1="24" y1="23" x2="30" y2="29" stroke="#fff" stroke-width="4" stroke-linecap="round"/></svg>
    </div>
  </div>
</header>

<nav class="nav abs">
  <ul>
    <li class="active">Home</li>
    <li>Services</li>
    <li>About Us</li>
    <li>FAQ</li>
    <li>Contact Us</li>
  </ul>
</nav>

<div class="hero abs" role="img" aria-label="Photo of a smiling family lying on the lawn in front of their new home">
  <div class="hero-sky"></div>
  <div class="hero-fade"></div>
</div>
<div class="hero-panel abs">
  <h2>Home loans</h2>
  <ul>
    <li><svg width="20" height="20" viewBox="0 0 20 20"><circle cx="10" cy="10" r="7" fill="none" stroke="#2eade3" stroke-width="3"/></svg>Home buyers</li>
    <li><svg width="20" height="20" viewBox="0 0 20 20"><circle cx="10" cy="10" r="7" fill="none" stroke="#2eade3" stroke-width="3"/></svg>First home buyers</li>
    <li><svg width="20" height="20" viewBox="0 0 20 20"><circle cx="10" cy="10" r="7" fill="none" stroke="#2eade3" stroke-width="3"/></svg>Over 20 lenders</li>
  </ul>
  <span class="btn-small">Learn More</span>
</div>
<div class="dots abs"><i></i><i></i><i class="on"></i></div>

<div class="dropdown abs">
  <a>Home loan</a>
  <a>Investment loan</a>
  <a>Refinancing</a>
  <a>Business loan</a>
</div>

<section class="welcome abs">
  <h1>WELCOME&nbsp; TO CORVELLA LENDING</h1>
  <p>At Corvella Lending we work hard to find the right loan for our customers. We do that because we are backed by sound industry knowledge, professional experience and a great customer service approach.</p>
  <p>Corvella Lending guarantees that we will always tailor the best solution for your individual lending needs.</p>
  <p>We can do that because we have access to a wide variety of lending options from major banks to non-bank lenders and we are committed to finding the right lending product for you.</p>
  <p>There are many different loan products in the marketplace. Corvella Lending has access to a wide panel of lenders which means we can access bank and non-bank lenders that meet the individual needs of our customers.</p>
  <p>Contact <strong>Corvella Lending</strong> today on: <em>1800 555 210</em> to find out more.</p>
</section>
<div class="divider abs"></div>

<section class="offers abs">
  <div class="offers-head">We offer a unique approach to help you find the right:</div>
</section>
<div class="offers-glow abs"></div>

<article class="card abs" style="left:87px">
  <h3>Home Loan</h3>
  <ul><li>Home buyers</li><li>First home buyers</li><li>Over 20 lenders</li></ul>
  <span class="more">Learn more</span>
</article>
<article class="card abs" style="left:353px">
  <h3>Investment Loan</h3>
  <ul><li>Property investment loans</li><li>Interest only loans</li></ul>
  <span class="more">Learn more</span>
</article>
<article class="card abs" style="left:620px">
  <h3>Refinancing</h3>
  <ul><li>Refinancing for the best rate</li><li>Upsizing or downsizing Change from a variable to a fixed rate</li></ul>
  <span class="more">Learn more</span>
</article>
<article class="card abs" style="left:884px">
  <h3>Business Loan &amp; Business Finance</h3>
  <ul><li>Long term</li><li>Short term</li><li>Equipment and Leasing</li></ul>
  <span class="more">Learn more</span>
</article>

<div class="borrow abs">
  <svg width="72" height="82" viewBox="0 0 72 82"><rect x="2" y="2" width="68" height="78" rx="6" fill="#1d9bd3" stroke="#7fd0f2" stroke-width="2"/><path d="M28 14h16v28h12L36 66 16 42h12z" fill="#0a4a6e"/></svg>
  <span>FIND OUT HOW MUCH<br>YOU COULD BORROW</span>
</div>

<section class="box abs" style="left:50px;width:339px">
  <div class="box-head">Client testimonial</div>
  <div class="box-body">
    "Lorem ipsum dolor sit amet, consectetur adipisicing elit, sed do eiusmod tempor incididunt ut labore et dolore magna aliqua, consectetur adipisicing elit, sed do eiusmod tempor"
    <div class="sign">Dale Pritchard<small>Worker</small></div>
  </div>
  <span class="btn-small">Read more</span>
</section>

<section class="box abs" style="left:428px;width:340px">
  <div class="box-head">Latest News</div>
  <div class="box-body">
    <div class="news-item"><span class="news-date">(April 18, 2012)</span><br>Lorem ipsum dolor sit amet, consectetur adipisicing elit.</div>
    <div class="news-item"><span class="news-date">(April 18, 2012)</span><br>Lorem ipsum dolor sit amet, consectetur adipisicing elit.</div>
  </div>
  <span class="btn-small">Read more</span>
</section>

<section class="box abs" style="left:809px;width:340px">
  <div class="box-head">Contact us</div>
  <div class="box-body contact-body">
    <p>You can contact us by using the contact information below or by sending us a message via <a>our contact form</a>.</p>
    <p>Corvella Lending, CA, USA</p>
    <p><span class="hl">Phone:</span> 1800 555 210</p>
    <p><span class="hl">Email:</span> office@corvellalending.com</p>
  </div>
</section>

<footer class="footer abs">
  <span class="copy">© 2012 Corvella Lending</span>
  <nav><span>home</span><span>services</span><span>about us</span><span>faq</span><span>contact us</span></nav>
  <div class="follow">Follow us: <i></i><i></i><i></i></div>
</footer>

</body>
</html>
```